New web design project for COVID-19 sanitisation product

Brochure style web site for 2 x products, including a home page, one product page per product (two in total), an FAQ page, a contact information page, and a contact form for enquiries.

I will upload the PDF sheets where all the assets can be taken from as far as content.

I will upload our logo which of course is to featured and the colours for this used as the basis for the web site look and feel. The logo font is Eurostile extended so this where practical should be used as well.

Target Market(s)

Business to business - education, hospitality, retail outlets such as banks, fast food

Industry/Entity Type

Business to business - sanitisation

Coding

Coded - Design and coding required

Number of Pages Required

5+ page

Font styles to use
Other font styles liked:
• Eurostile extended is the logo font.

Colors
0094D4
00A9DD
6FCCEA
C7EBF8
E9F6FB

Requirements
Must have
• Brochure style web site for 2 x products, FAQ, contact information and a contact form for enquiries

```html
<!DOCTYPE html>
<html lang="en">
<head>
<meta charset="utf-8">
<title>Brightwell Systems – Clarion Hygiene+</title>
<link rel="stylesheet" href="https://fonts.googleapis.com/css2?family=Montserrat:wght@500;600;700;800&family=Nunito+Sans:wght@400;600;700&display=swap">
<style>
  :root{
    --navy:#124a7c;
    --sky:#62bde9;
    --button:#5bbcec;
    --royal:#0a1fe0;
    --steel:#5b8ab8;
    --ink:#222a33;
    --muted:#3b4450;
    --card:#f3f4f5;
    --white:#ffffff;
    --dark:#14181c;
    --heading:"Montserrat", sans-serif;
    --body:"Nunito Sans", sans-serif;
  }
  *{box-sizing:border-box;margin:0;padding:0}
  html,body{width:1200px;height:3357px;overflow:hidden}
  body{position:relative;background:var(--white);font-family:var(--body);color:var(--ink)}
  .abs{position:absolute}
  .btn{position:absolute;display:flex;align-items:center;justify-content:center;background:var(--button);color:var(--white);font-family:var(--heading);font-weight:700;font-size:13px;letter-spacing:.04em;text-transform:uppercase}

  /* header */
  .site-header{position:absolute;left:0;top:0;width:1200px;height:85px;background:var(--white);z-index:3}
  .brand{position:absolute;display:flex;align-items:center;gap:8px;font-family:var(--heading);font-weight:700;color:var(--navy);text-transform:uppercase}
  .brand-dot{width:22px;height:22px;border-radius:50%;background:var(--navy)}
  .site-header .brand{left:72px;top:28px;font-size:13px;letter-spacing:.02em}
  .nav{position:absolute;top:31px;font-family:var(--heading);font-size:12.5px;font-weight:500;color:#6b7580;letter-spacing:.04em}
  .nav.active{color:var(--ink);font-weight:600}

  /* hero */
  .hero{position:absolute;left:0;top:85px;width:1200px;height:557px;background:linear-gradient(90deg,#fdfdfe 0%,#f2f4f7 30%,#d8e4ee 48%,#9fc2dc 60%,#c9d9e6 78%,#eef1f3 100%)}
  .hero-title{position:absolute;left:70px;top:160px;font-family:var(--heading);font-weight:800;font-size:52px;line-height:66px;color:var(--navy);letter-spacing:.02em}
  .hero-sub{position:absolute;left:70px;top:287px;font-family:var(--heading);font-weight:500;font-size:22px;color:var(--navy);letter-spacing:.02em}
  .slider-dot{position:absolute;width:12px;height:12px;border-radius:50%;border:1.5px solid var(--white)}

  /* solution */
  .solution{position:absolute;left:0;top:642px;width:1200px;height:396px;background:var(--sky);overflow:hidden}
  .section-title{position:absolute;left:0;width:1200px;text-align:center;font-family:var(--heading);font-weight:700;font-size:29px}
  .feature{position:absolute;width:180px;text-align:center}
  .feature-label{margin-top:14px;font-family:var(--heading);font-weight:600;font-size:17px;color:var(--white)}

  /* process */
  .step-art{position:absolute;width:205px;height:135px;background:linear-gradient(180deg,#ffffff 0%,#f3f7fb 55%,#8fd8cf 78%,#56c1b6 100%);box-shadow:0 2px 8px rgba(0,0,0,.18)}
  .step-badge{position:absolute;width:44px;height:44px;border-radius:50%;background:var(--button);border:3px solid var(--white);box-shadow:0 1px 4px rgba(0,0,0,.2);color:var(--white);font-family:var(--heading);font-size:10px;font-weight:600;line-height:12px;text-align:center;padding-top:8px}
  .step-text{position:absolute;width:310px;text-align:center;font-size:14.5px;line-height:22px;color:var(--ink)}

  /* products */
  .product-band{position:absolute;left:0;width:1200px;overflow:hidden}
  .eyebrow{position:absolute;font-family:var(--heading);font-weight:500;font-size:15px;color:var(--white);letter-spacing:.02em}
  .product-title{position:absolute;font-family:var(--heading);font-weight:700;font-size:29px;color:var(--white);letter-spacing:.02em}
  .product-copy{position:absolute;font-family:var(--heading);font-weight:500;font-size:18.5px;line-height:27px;color:var(--white)}
  .bottle{position:absolute;border-radius:30px 30px 24px 24px;background:linear-gradient(90deg,#e3e6e9,#ffffff 40%,#f1f2f4 80%,#d9dde0);z-index:2}
  .bottle-label{position:absolute;border-radius:2px}

  /* faq */
  .faq-item{position:absolute;width:435px;background:var(--card);border:1px solid #e3e5e7;display:flex;align-items:center;padding:0 16px;font-family:var(--heading);font-weight:500;font-size:15px;line-height:22px;color:var(--ink)}
  .faq-num{width:30px;flex:none;color:#444}
  .faq-q{flex:1}
  .faq-plus{width:22px;height:22px;border-radius:50%;background:var(--white);display:flex;align-items:center;justify-content:center;font-size:16px;font-weight:700;flex:none}

  /* contact */
  .contact{position:absolute;left:0;top:2756px;width:1200px;height:601px;background:linear-gradient(90deg,#3a4350 0%,#20262d 30%,#14181c 60%,#0f1215 100%);overflow:hidden}
  .field{position:absolute;background:var(--white);border:1px solid #cfd3d7;font-family:var(--heading);font-size:11px;font-weight:500;color:#333;padding:12px 12px}
  .footer-info{position:absolute;display:flex;align-items:center;gap:10px;color:var(--white);font-family:var(--heading);font-size:13px;line-height:21px;z-index:2}
  .info-icon{width:40px;height:40px;border-radius:50%;background:var(--white);display:flex;align-items:center;justify-content:center;flex:none}
  .social{position:absolute;width:30px;height:30px;border-radius:50%;background:var(--white);z-index:2}
  .copyright{position:absolute;left:0;top:3311px;width:1200px;text-align:center;font-family:var(--heading);font-size:12px;color:var(--white);z-index:2}
</style>
</head>
<body>

<header class="site-header">
  <div class="brand"><span class="brand-dot"></span>Brightwell Systems</div>
  <span class="nav active" style="left:644px">HOME</span>
  <span class="nav" style="left:724px">PRODUCT</span>
  <span class="nav" style="left:826px">FAQ</span>
  <span class="nav" style="left:891px">CONTACT</span>
  <a class="btn" style="left:998px;top:20px;width:130px;height:39px;font-size:12.5px">Enquiry Now</a>
</header>

<section class="hero">
  <div class="abs" role="img" aria-label="Mother helping her young daughter wash her hands at a sink" style="left:430px;top:0;width:770px;height:557px"></div>
  <h1 class="hero-title">CLARION<br>HYGIENE+</h1>
  <p class="hero-sub">SAFE. SCIENTIFIC. SELF-SANITISING.</p>
  <a class="btn" style="left:72px;top:332px;width:148px;height:43px">View Product</a>
  <span class="slider-dot" style="left:1116px;top:254px"></span>
  <span class="slider-dot" style="left:1116px;top:287px;background:var(--white)"></span>
</section>

<section class="solution">
  <h2 class="section-title" style="top:56px;color:var(--white)">CLARION SOLUTION</h2>
  <div class="feature" style="left:167px;top:137px">
    <svg width="180" height="126" viewBox="0 0 180 126"><circle cx="90" cy="63" r="61" fill="none" stroke="#fff" stroke-width="2" stroke-dasharray="4 4"/><circle cx="90" cy="63" r="50" fill="#fff"/><path d="M90 36 C80 52 72 62 72 72 a18 18 0 0 0 36 0 c0-10-8-20-18-36z" fill="none" stroke="var(--navy)" stroke-width="3"/><path d="M96 70 a8 8 0 0 1-6 12" fill="none" stroke="var(--navy)" stroke-width="3"/></svg>
    <div class="feature-label">WATER BASED</div>
  </div>
  <div class="feature" style="left:391px;top:137px">
    <svg width="180" height="126" viewBox="0 0 180 126"><circle cx="90" cy="63" r="61" fill="none" stroke="#fff" stroke-width="2" stroke-dasharray="4 4"/><circle cx="90" cy="63" r="50" fill="#fff"/><g fill="none" stroke="var(--navy)" stroke-width="2.5"><path d="M90 38 v26 M90 56 l-8 8 M90 56 l8 8"/><path d="M82 50 c-10 2-16 14-16 28 0 6 4 8 10 6 6-2 8-6 8-12 v-18"/><path d="M98 50 c10 2 16 14 16 28 0 6-4 8-10 6-6-2-8-6-8-12 v-18"/></g></svg>
    <div class="feature-label">BREATHABLE</div>
  </div>
  <div class="feature" style="left:617px;top:137px">
    <svg width="180" height="126" viewBox="0 0 180 126"><circle cx="90" cy="63" r="61" fill="none" stroke="#fff" stroke-width="2" stroke-dasharray="4 4"/><circle cx="90" cy="63" r="50" fill="#fff"/><g fill="none" stroke="var(--navy)" stroke-width="3" stroke-linecap="round"><path d="M66 50 q6-6 12 0 t12 0 t12 0 t12 0"/><path d="M66 60 q6-6 12 0 t12 0 t12 0 t12 0"/><path d="M66 70 q6-6 12 0 t12 0 t12 0 t12 0"/><path d="M66 80 q6-6 12 0 t12 0 t12 0 t12 0"/></g></svg>
    <div class="feature-label">ODOURLESS</div>
  </div>
  <div class="feature" style="left:843px;top:137px">
    <svg width="180" height="126" viewBox="0 0 180 126"><circle cx="90" cy="63" r="61" fill="none" stroke="#fff" stroke-width="2" stroke-dasharray="4 4"/><circle cx="90" cy="63" r="50" fill="#fff"/><path d="M90 36 l22 8 v18 c0 16-10 24-22 28 c-12-4-22-12-22-28 v-18z" fill="none" stroke="var(--navy)" stroke-width="3"/><path d="M80 63 l7 7 l13-14" fill="none" stroke="var(--navy)" stroke-width="3" stroke-linecap="round"/></svg>
    <div class="feature-label">SAFE</div>
  </div>
</section>

<section class="process">
  <h2 class="section-title" style="top:1092px;color:var(--navy)">ITS PROCESS</h2>

  <div class="step-art" role="img" aria-label="Diagram of airborne microbes landing on the positively charged coating" style="left:152px;top:1190px"></div>
  <div class="step-badge" style="left:123px;top:1234px">STEP<br>1.</div>
  <div class="step-art" role="img" aria-label="Diagram of nano particles dissolving the outer protein layer of microbes" style="left:508px;top:1190px"></div>
  <div class="step-badge" style="left:475px;top:1234px">STEP<br>2.</div>
  <div class="step-art" role="img" aria-label="Diagram of silver ions rupturing the microbe's RNA" style="left:869px;top:1190px"></div>
  <div class="step-badge" style="left:835px;top:1234px">STEP<br>3.</div>

  <svg class="abs" style="left:382px;top:1238px" width="70" height="36" viewBox="0 0 70 36"><path d="M4 18 q26 18 54 0" fill="none" stroke="#5b6570" stroke-width="5" stroke-linecap="round"/><path d="M50 6 l16 6 l-12 12z" fill="#5b6570"/></svg>
  <svg class="abs" style="left:748px;top:1238px" width="70" height="36" viewBox="0 0 70 36"><path d="M4 18 q26 18 54 0" fill="none" stroke="#5b6570" stroke-width="5" stroke-linecap="round"/><path d="M50 6 l16 6 l-12 12z" fill="#5b6570"/></svg>

  <p class="step-text" style="left:85px;top:1361px">When microbes such as bacteria,viruses and fungi which are negatively charged come into contact with our protective coating, the positively charged Quats contained in the polymer immobilise the microbe.</p>
  <p class="step-text" style="left:445px;top:1361px;width:240px;left:480px">Quats or Silver nano particles dissolves the outer protein layer of the microbes.</p>
  <p class="step-text" style="left:804px;top:1361px">The silver ions are now able to inactivate the microbe and rupture the RNA in a virus or DNA in bacteria which prevents them from replication.</p>
</section>

<section class="product-band" style="top:1540px;height:356px;background:var(--royal)">
  <div class="abs" role="img" aria-label="Woman relaxing on a sofa beneath a wall air conditioner" style="left:700px;top:0;width:500px;height:356px;background:linear-gradient(90deg,#dfe3e6,#eef0f2 50%,#c9d2d6)"></div>
  <span class="eyebrow" style="left:73px;top:69px">INTRODUCING</span>
  <h3 class="product-title" style="left:73px;top:95px">CLARION AC+</h3>
  <p class="product-copy" style="left:73px;top:146px;width:460px">Our Clarion AC+ super charges your existing air conditioner enabling it to kill 99% of thebacteria and viruses it filters.</p>
  <a class="btn" style="left:73px;top:245px;width:148px;height:43px">View Product</a>
</section>
<div class="bottle" role="img" aria-label="Five litre container of Clarion AC+" style="left:700px;top:1515px;width:260px;height:411px">
  <div class="bottle-label" style="left:24px;top:138px;width:214px;height:200px;background:#111"></div>
  <div class="bottle-label" style="left:24px;top:138px;width:214px;height:38px;background:var(--royal)"></div>
</div>

<section class="product-band" style="top:1896px;height:361px;background:var(--steel)">
  <div class="abs" role="img" aria-label="Mother and daughter washing hands together" style="left:0;top:0;width:534px;height:361px;background:linear-gradient(90deg,#7fa7c4,#c7d6e2 50%,#e6ecf0)"></div>
  <span class="eyebrow" style="left:710px;top:81px">INTRODUCING</span>
  <h3 class="product-title" style="left:710px;top:108px">CLARION HYGIENE+</h3>
  <p class="product-copy" style="left:710px;top:158px;width:440px">24/7 self-sanitising protection for your surfaces lasting 90 days.</p>
  <a class="btn" style="left:710px;top:233px;width:149px;height:44px">View Product</a>
</section>
<div class="bottle" role="img" aria-label="Five litre container of Clarion Hygiene+" style="left:244px;top:1853px;width:258px;height:404px">
  <div class="bottle-label" style="left:20px;top:137px;width:216px;height:196px;background:#111"></div>
  <div class="bottle-label" style="left:20px;top:137px;width:216px;height:38px;background:#45cfae"></div>
</div>

<section class="faq">
  <h2 class="section-title" style="top:2340px;color:var(--ink);font-weight:600">FAQ</h2>
  <div class="faq-item" style="left:158px;top:2401px;height:67px"><span class="faq-num">1.</span><span class="faq-q">Is Clarion Hygiene+ safe for my  children, pets and vulnerable family  members?</span><span class="faq-plus">+</span></div>
  <div class="faq-item" style="left:607px;top:2401px;height:67px"><span class="faq-num">2.</span><span class="faq-q">How many coats of Clarion Hygiene+ do I need to apply?</span><span class="faq-plus">+</span></div>
  <div class="faq-item" style="left:158px;top:2479px;height:54px"><span class="faq-num">3.</span><span class="faq-q">Can I use Clarion Hygiene+ outside?</span><span class="faq-plus">+</span></div>
  <div class="faq-item" style="left:607px;top:2479px;height:54px"><span class="faq-num">4.</span><span class="faq-q">Is Clarion Hygiene+ safe for my pets?</span><span class="faq-plus">+</span></div>
  <div class="faq-item" style="left:158px;top:2547px;height:72px"><span class="faq-num">5.</span><span class="faq-q">Does Clarion Hygiene+ have an expiry date?</span><span class="faq-plus">+</span></div>
  <div class="faq-item" style="left:607px;top:2547px;height:72px"><span class="faq-num">6.</span><span class="faq-q">Is Clarion Hygiene+ safe to apply to my timber furniture?</span><span class="faq-plus">+</span></div>
  <a class="btn" style="left:534px;top:2638px;width:132px;height:39px;font-weight:600">View FAQ</a>
</section>

<section class="contact">
  <div class="abs" role="img" aria-label="Child washing hands under a running kitchen tap" style="left:0;top:0;width:640px;height:480px;background:linear-gradient(90deg,#6f7e91,#394350 45%,#1a1f24)"></div>
  <svg class="abs" style="left:0;top:0" width="1200" height="601" viewBox="0 0 1200 601"><path d="M0 302 C180 280 320 320 520 370 C700 414 860 400 1000 420 C1100 434 1160 460 1200 476 L1200 601 L0 601Z" fill="var(--royal)"/></svg>
  <h2 class="abs" style="left:694px;top:48px;font-family:var(--heading);font-weight:700;font-size:28px;color:var(--white)">CONTACT US</h2>
  <div class="field" style="left:694px;top:95px;width:214px;height:39px">First Name :</div>
  <div class="field" style="left:913px;top:95px;width:215px;height:39px">Last Name :</div>
  <div class="field" style="left:694px;top:140px;width:214px;height:40px">Email :</div>
  <div class="field" style="left:913px;top:140px;width:215px;height:40px">Phone No :</div>
  <div class="field" style="left:694px;top:190px;width:434px;height:98px">Message :</div>
  <a class="btn" style="left:693px;top:298px;width:130px;height:38px">Submit Now</a>
</section>

<footer>
  <div class="brand" style="left:74px;top:3230px;font-size:13px;color:var(--white);z-index:2"><span class="brand-dot" style="background:var(--white)"></span>Brightwell Systems</div>
  <div class="footer-info" style="left:319px;top:3212px">
    <span class="info-icon"><svg width="20" height="14" viewBox="0 0 20 14"><rect x="1" y="1" width="18" height="12" rx="1" fill="none" stroke="var(--sky)" stroke-width="1.8"/><path d="M1 1 l9 7 l9-7" fill="none" stroke="var(--sky)" stroke-width="1.8"/></svg></span>
    <span>Mail Us :<br>hello@brightwellsystems.com</span>
  </div>
  <div class="footer-info" style="left:628px;top:3212px">
    <span class="info-icon"><svg width="18" height="18" viewBox="0 0 18 18"><path d="M4 1 l3 4 -2 2 c1 3 3 5 6 6 l2-2 4 3 -2 3 C8 17 1 10 1 3z" fill="var(--sky)"/></svg></span>
    <span>Call Us :<br>555-010-2040</span>
  </div>
  <span class="social" style="left:984px;top:3217px"></span>
  <span class="social" style="left:1022px;top:3217px"></span>
  <span class="social" style="left:1059px;top:3217px"></span>
  <span class="social" style="left:1096px;top:3217px"></span>
  <p class="copyright">© 2021 Brightwell Systems. All rights reserved.</p>
</footer>

</body>
</html>
```